IT Company based on Biology Business Needs a Business Card Design

We need a business card design for a new company called 'Lumen CELL'. We develop the machine learning solutions especially focused on deep learning algorithms for biology industry. Our initial product is a vision detection on biological images to help doctors diagnose the symptoms. We would like to see designs that use the color green.

Industry/Entity Type

Business

```html
<!DOCTYPE html>
<html lang="en">
<head>
<meta charset="UTF-8">
<title>Lumen CELL – Business Card</title>
<link href="https://fonts.googleapis.com/css2?family=Open+Sans:wght@400;600;700&display=swap" rel="stylesheet">
<style>
  :root {
    --canvas-bg: #e4e6e8;
    --card-bg: #f1f5f9;
    --green-dark: #16873a;
    --green-mid: #4fae3a;
    --green-light: #7cc242;
    --white: #ffffff;
  }
  * { margin: 0; padding: 0; box-sizing: border-box; }
  html, body {
    width: 1200px; height: 880px; overflow: hidden;
    background: var(--canvas-bg);
    font-family: "Open Sans", sans-serif;
  }
  .canvas {
    width: 1200px; height: 880px;
    display: flex; flex-direction: column; align-items: center; justify-content: center;
    gap: 44px;
  }
  .card {
    position: relative;
    width: 660px; height: 377px;
    background: var(--card-bg);
    box-shadow: 0 6px 18px rgba(0,0,0,0.18);
    overflow: hidden;
  }
  .brand {
    position: absolute;
    display: flex; align-items: center; gap: 14px;
    z-index: 2;
  }
  .brand-dot {
    width: 30px; height: 30px; border-radius: 50%;
    background: var(--green-mid);
  }
  .brand-name {
    font-weight: 600; font-size: 46px; letter-spacing: -1px;
    color: var(--green-mid); line-height: 1;
  }
  /* back card */
  .card-back .brand { left: 190px; top: 128px; }
  .card-back .email {
    position: absolute; left: 190px; top: 222px;
    font-size: 19px; font-weight: 600; color: var(--green-light);
  }
  /* front card */
  .card-front .brand { left: 56px; top: 150px; }
  .person {
    position: absolute; right: 52px; top: 42px; text-align: right;
    z-index: 2;
  }
  .person-name {
    font-size: 24px; font-weight: 700; color: var(--green-dark); letter-spacing: 0.5px;
  }
  .person-title {
    font-size: 15px; font-weight: 600; color: var(--green-light); letter-spacing: 2px; margin-top: 4px;
  }
  .contacts {
    position: absolute; right: 46px; top: 142px;
    list-style: none; text-align: right;
    z-index: 2;
  }
  .contacts li {
    display: flex; align-items: center; justify-content: flex-end; gap: 8px;
    font-size: 17px; color: var(--green-dark); line-height: 26px; letter-spacing: 0.6px;
  }
  .contacts svg { width: 14px; height: 14px; fill: var(--green-dark); }
  .swoosh { position: absolute; left: 0; top: 0; width: 660px; height: 377px; z-index: 1; }
</style>
</head>
<body>
<main class="canvas">
  <section class="card card-back">
    <div class="brand">
      <span class="brand-dot"></span>
      <span class="brand-name">Lumen CELL</span>
    </div>
    <p class="email">Email: hello@lumencell.com</p>
  </section>

  <section class="card card-front">
    <div class="brand">
      <span class="brand-dot"></span>
      <span class="brand-name">Lumen CELL</span>
    </div>
    <div class="person">
      <p class="person-name">TOMAS VERHAL</p>
      <p class="person-title">PREZIDENT</p>
    </div>
    <ul class="contacts">
      <li>+61 (0)400 555 018
        <svg viewBox="0 0 14 14"><path d="M4 0h6a1 1 0 0 1 1 1v12a1 1 0 0 1-1 1H4a1 1 0 0 1-1-1V1a1 1 0 0 1 1-1zm0 2v9h6V2z"/></svg></li>
      <li>+61 (0)2 5550 1234
        <svg viewBox="0 0 14 14"><path d="M1 5c0-2 3-3 6-3s6 1 6 3v1h-3V5H4v1H1zM3 7h8l2 6H1z"/></svg></li>
      <li>www.lumencell.com
        <svg viewBox="0 0 14 14"><circle cx="7" cy="7" r="6.5"/></svg></li>
    </ul>
    <svg class="swoosh" viewBox="0 0 660 377" preserveAspectRatio="none">
      <path fill="var(--green-light)" d="M0,377 L0,348 C220,296 440,276 660,258 L660,377 Z"/>
      <path fill="var(--white)" d="M0,340 C220,288 440,266 660,246 L660,258 C440,276 220,296 0,348 Z"/>
      <path fill="var(--green-dark)" d="M30,334 C230,286 440,262 660,240 L660,249 C440,270 230,293 30,340 Z"/>
      <path fill="var(--green-mid)" d="M250,292 C400,268 540,252 660,236 L660,241 C540,256 400,272 250,295 Z"/>
    </svg>
  </section>
</main>
</body>
</html>
```